Engineering Consultant Business Card

I'm starting a new business as a high-end engineering consultant in a niche field. I've attached the jpg for my logo plus the branding guideline document that I've been following. You can see my business website here: www.tarvikworks.com
I'd like a business card that has the logo on one side, then the other side has (in any order): Tarvik Works, Inc.
Dana Whitlock
President and Chief EMC Engineer
www.tarvikworks.com
dana@tarvikworks.com
Optional: motto "We will solve your EMC problems as early as possible—ideally before they even start."
I'm not planning on including a phone number
Target Market(s)
Businesses, especially makers of electronics hardware
Industry/Entity Type
Electrical engineering
Contact Information for Business Card
Company name, my name, website, email

```html
<!DOCTYPE html>
<html lang="en">
<head>
<meta charset="utf-8">
<title>Tarvik Works, Inc. — Business Card</title>
<link rel="stylesheet" href="https://fonts.googleapis.com/css2?family=Montserrat:wght@400;500;700&display=swap">
<style>
  :root {
    --page-bg: #e4e2e3;
    --card-white: #ffffff;
    --brand-blue: #2e47a0;
    --brand-blue-deep: #283f92;
    --pattern-silver: #6f7fbf;
    --ink: #1d1d1f;
    --icon-white: #ffffff;
  }
  * { box-sizing: border-box; margin: 0; padding: 0; }
  html, body {
    width: 1200px;
    height: 1108px;
    overflow: hidden;
    background: var(--page-bg);
    font-family: "Montserrat", Arial, sans-serif;
  }
  .canvas {
    position: relative;
    width: 1200px;
    height: 1108px;
  }

  /* Front of card */
  .card-front {
    position: absolute;
    left: 237px;
    top: 67px;
    width: 729px;
    height: 437px;
    background: var(--card-white);
  }
  .side-band {
    position: absolute;
    left: 0;
    top: 0;
    width: 35px;
    height: 100%;
    background: var(--brand-blue);
  }
  .identity {
    position: absolute;
    right: 46px;
    top: 198px;
    text-align: right;
  }
  .person-name {
    font-weight: 700;
    font-size: 27px;
    line-height: 1.1;
    color: var(--brand-blue);
    letter-spacing: 0.2px;
  }
  .person-title {
    font-weight: 500;
    font-size: 15.5px;
    color: var(--ink);
    margin-top: 3px;
  }
  .contact-list {
    position: absolute;
    left: 0;
    top: 344px;
    list-style: none;
  }
  .contact-item {
    position: relative;
    height: 29px;
    display: flex;
    align-items: center;
  }
  .contact-icon {
    position: absolute;
    left: 10px;
    width: 15px;
    height: 15px;
  }
  .contact-text {
    margin-left: 47px;
    font-size: 15.5px;
    font-weight: 400;
    color: var(--ink);
  }

  /* Back of card */
  .card-back {
    position: absolute;
    left: 244px;
    top: 580px;
    width: 728px;
    height: 436px;
    background: var(--brand-blue);
    overflow: hidden;
  }
  .back-pattern {
    position: absolute;
    inset: 0;
    background: linear-gradient(100deg, var(--brand-blue-deep) 0%, var(--brand-blue) 55%, var(--pattern-silver) 100%);
  }
  .back-wordmark {
    position: absolute;
    left: 416px;
    top: 288px;
    transform: translate(-50%, -50%);
    display: flex;
    align-items: center;
    gap: 9px;
    color: var(--card-white);
    font-weight: 700;
    font-size: 17px;
    letter-spacing: 1px;
    white-space: nowrap;
  }
  .wordmark-dot {
    width: 12px;
    height: 12px;
    border-radius: 50%;
    background: var(--card-white);
  }
</style>
</head>
<body>
<main class="canvas">

  <section class="card-front" aria-label="Business card front">
    <div class="side-band"></div>
    <div class="identity">
      <h1 class="person-name">Dana Whitlock</h1>
      <p class="person-title">President &amp; Chief EMC Engineer</p>
    </div>
    <ul class="contact-list">
      <li class="contact-item">
        <svg class="contact-icon" viewBox="0 0 16 16" aria-hidden="true">
          <rect x="1.5" y="3.5" width="13" height="9" rx="1" fill="var(--icon-white)"/>
          <path d="M1.8 4 L8 8.6 L14.2 4" fill="none" stroke="var(--brand-blue)" stroke-width="1.2"/>
        </svg>
        <span class="contact-text">dana@tarvikworks.com</span>
      </li>
      <li class="contact-item">
        <svg class="contact-icon" viewBox="0 0 16 16" aria-hidden="true">
          <circle cx="8" cy="8" r="6.5" fill="var(--icon-white)"/>
          <path d="M4 5.5 Q6 4.5 7 6 Q6.5 8 5 8.5 Q4 9.5 4.5 11 M9.5 3.5 Q10.5 5.5 12 5.5 M10 9 Q11.5 9 11.5 11 Q10 12.5 9 12" fill="none" stroke="var(--brand-blue)" stroke-width="1.1"/>
        </svg>
        <span class="contact-text">www.tarvikworks.com</span>
      </li>
    </ul>
  </section>

  <section class="card-back" aria-label="Business card back">
    <div class="back-pattern" role="img" aria-label="Repeating tone-on-tone brand pattern fading to silver foil at the right"></div>
    <div class="back-wordmark">
      <span class="wordmark-dot"></span>
      <span class="wordmark-name">TARVIK WORKS</span>
    </div>
  </section>

</main>
</body>
</html>
```